New Zealand Marlborough Sauvignon Blanc wine packaging design

We need packaging design for our new wine brand, Dunmore Hale. The wine is a New Zealand Marlborough Sauvignon Blanc. We would like the packaging will portray elegance and style with an understated label. We are looking for a label that portrays the elegance of the French Riviera. The label should be round or pill shaped.
Updates

Industry/Entity Type

Wine

Font styles to use
Serif
Sans Serif

Requirements
Must have
• The words in order of importance: Dunmore Hale, Sauvignon Blanc, Marlborough, New Zealand. It should be fit to the bottle posted in the links
Nice to have
• a pill shape or circular shape
Should not have
• Illustrations of wine bottles, wine glasses, or grapes

```html
<!DOCTYPE html>
<html lang="en">
<head>
<meta charset="utf-8">
<title>Dunmore Hale — Marlborough Sauvignon Blanc Label</title>
<link rel="stylesheet" href="https://fonts.googleapis.com/css2?family=Cinzel:wght@400&family=Playfair+Display:ital,wght@1,700&family=Montserrat:wght@600&display=swap">
<style>
  :root {
    --glass: #0b0b0b;
    --gold: #e7b93f;
    --gold-light: #f2c94e;
    --gold-deep: #c99a2a;
    --ink: #141414;
    --region-ink: #2a2a2a;
    --white: #f4f4f4;
  }
  * { margin: 0; padding: 0; box-sizing: border-box; }
  html, body {
    width: 1200px;
    height: 1200px;
    overflow: hidden;
    background: var(--glass);
  }
  .label {
    position: relative;
    width: 1200px;
    height: 1200px;
    background: var(--glass);
  }
  .brand-name {
    position: absolute;
    left: 0;
    right: 0;
    top: 290px;
    text-align: center;
    font-family: "Cinzel", serif;
    font-weight: 400;
    font-size: 76px;
    line-height: 1.2;
    letter-spacing: 6px;
    color: var(--white);
  }
  .variety-band {
    position: absolute;
    left: 0;
    top: 690px;
    width: 1200px;
    height: 230px;
    background: linear-gradient(90deg, var(--gold-deep) 0%, var(--gold-light) 45%, var(--gold) 100%);
    display: flex;
    flex-direction: column;
    align-items: center;
    justify-content: center;
  }
  .variety-band::before,
  .variety-band::after {
    content: "";
    position: absolute;
    left: 0;
    right: 0;
    height: 4px;
    background: var(--ink);
  }
  .variety-band::before { top: 20px; }
  .variety-band::after { bottom: 20px; }
  .variety {
    font-family: "Playfair Display", serif;
    font-style: italic;
    font-weight: 700;
    font-size: 86px;
    color: var(--ink);
    letter-spacing: 2px;
    line-height: 1.05;
  }
  .region {
    font-family: "Montserrat", sans-serif;
    font-weight: 600;
    font-size: 54px;
    color: var(--region-ink);
    letter-spacing: 1px;
    margin-top: 4px;
  }
  .country {
    position: absolute;
    left: 0;
    right: 0;
    top: 1000px;
    text-align: center;
    font-family: "Cinzel", serif;
    font-weight: 400;
    font-size: 50px;
    color: var(--white);
    letter-spacing: 3px;
  }
</style>
</head>
<body>
  <main class="label">
    <h1 class="brand-name">DUNMORE HALE</h1>
    <section class="variety-band">
      <p class="variety">Sauvignon Blanc</p>
      <p class="region">MARLBOROUGH</p>
    </section>
    <p class="country">NEW ZEALAND</p>
  </main>
</body>
</html>
```